Saltwater Aquarium Store Business Cards

Im looking for a fresh new look to my out dated business cards for my company. Its a retail saltwater aquarium store. I want like a modern design that has an aquatic underwater feel. Needs to have certain business information as well. I would like to incorporate my logo as well. and a qr code for our website.
Logo Text
already have a logo

```html
<!DOCTYPE html>
<html lang="en">
<head>
<meta charset="utf-8">
<title>Reef Harbor Aquatics – Business Cards</title>
<link rel="stylesheet" href="https://fonts.googleapis.com/css2?family=Montserrat:wght@400;500;700;800&display=swap">
<style>
  :root {
    --page-bg: #3a3a3c;
    --card-white: #ffffff;
    --card-navy: #0b2741;
    --navy-deep: #04203a;
    --brand-navy: #14314d;
    --brand-blue: #1e9ad6;
    --brand-coral: #e0525a;
    --text-dark: #2a2a2a;
    --text-grey: #444444;
    --divider: #555555;
  }
  * { box-sizing: border-box; margin: 0; padding: 0; }
  html, body {
    width: 1200px; height: 1200px; overflow: hidden;
    background: var(--page-bg);
    font-family: "Montserrat", sans-serif;
  }
  .sheet {
    position: relative; width: 1200px; height: 1200px;
    display: flex; flex-direction: column; align-items: center; justify-content: center; gap: 70px;
  }
  .card {
    position: relative; width: 700px; height: 400px; border-radius: 34px;
    box-shadow: 0 18px 40px rgba(0,0,0,.45);
    overflow: hidden;
  }
  .card--front { background: var(--card-white); }
  .card--back {
    background:
      radial-gradient(ellipse 60% 80% at 70% 20%, rgba(40,90,130,.35) 0%, rgba(40,90,130,0) 70%),
      linear-gradient(120deg, var(--navy-deep) 0%, var(--card-navy) 55%, #0e2f4d 100%);
  }

  .watermark {
    position: absolute; left: 270px; top: 70px; width: 260px; height: 300px;
    border-radius: 50% 50% 48% 52% / 40% 40% 60% 60%;
    background: radial-gradient(ellipse at 55% 70%, rgba(30,154,214,.16) 0%, rgba(224,82,90,.08) 55%, rgba(255,255,255,0) 75%);
  }
  .sheen {
    position: absolute; left: 250px; top: -60px; width: 140px; height: 560px;
    transform: rotate(18deg);
    background: linear-gradient(90deg, rgba(255,255,255,0) 0%, rgba(255,255,255,.07) 50%, rgba(255,255,255,0) 100%);
  }

  .brand { position: absolute; display: flex; align-items: center; gap: 14px; }
  .brand__dot { width: 46px; height: 46px; border-radius: 50%; background: var(--brand-blue); flex: none; }
  .brand__name { font-weight: 800; font-size: 36px; letter-spacing: .5px; white-space: nowrap; }
  .card--front .brand { left: 70px; top: 80px; }
  .card--front .brand__name { color: var(--brand-navy); }
  .card--back .brand { left: 50%; top: 50%; transform: translate(-50%, -50%); }
  .card--back .brand__dot { width: 60px; height: 60px; }
  .card--back .brand__name { color: #ffffff; font-size: 44px; }

  .person { position: absolute; left: 70px; bottom: 70px; padding-left: 16px; border-left: 5px solid var(--brand-blue); }
  .person__name { color: var(--brand-blue); font-size: 34px; font-weight: 500; line-height: 1; }
  .person__role { color: var(--text-grey); font-size: 22px; font-weight: 400; line-height: 1.1; margin-top: 2px; }

  .divider { position: absolute; left: 370px; top: 200px; width: 1px; height: 130px; background: var(--divider); }

  .contact { position: absolute; left: 395px; top: 190px; list-style: none; }
  .contact__item { display: flex; align-items: flex-start; gap: 10px; color: var(--text-dark); font-size: 15.5px; line-height: 1.35; margin-bottom: 8px; }
  .contact__icon { width: 18px; height: 18px; flex: none; margin-top: 2px; }
</style>
</head>
<body>
<main class="sheet">

  <section class="card card--front" aria-label="Business card front">
    <div class="watermark" role="img" aria-label="Faint enlarged brand emblem in pale blue and coral"></div>

    <div class="brand">
      <span class="brand__dot"></span>
      <span class="brand__name">Reef Harbor Aquatics</span>
    </div>

    <div class="divider"></div>

    <ul class="contact">
      <li class="contact__item">
        <svg class="contact__icon" viewBox="0 0 24 24"><path fill="#1e9ad6" d="M6.6 10.8a15.2 15.2 0 0 0 6.6 6.6l2.2-2.2a1 1 0 0 1 1-.25 11.4 11.4 0 0 0 3.6.57 1 1 0 0 1 1 1V20a1 1 0 0 1-1 1A17 17 0 0 1 3 4a1 1 0 0 1 1-1h3.5a1 1 0 0 1 1 1c0 1.25.2 2.450.57 3.57a1 1 0 0 1-.25 1z"/></svg>
        <span>(555) 014-2287</span>
      </li>
      <li class="contact__item">
        <svg class="contact__icon" viewBox="0 0 24 24" fill="none" stroke="#1e9ad6" stroke-width="1.8"><circle cx="12" cy="12" r="9.5"/><ellipse cx="12" cy="12" rx="4.5" ry="9.5"/><path d="M2.5 12h19M4 7h16M4 17h16"/></svg>
        <span>reefharboraquatics.example</span>
      </li>
      <li class="contact__item">
        <svg class="contact__icon" viewBox="0 0 24 24"><path fill="#1e9ad6" d="M12 2a7 7 0 0 0-7 7c0 5.2 7 13 7 13s7-7.8 7-13a7 7 0 0 0-7-7zm0 9.5A2.5 2.5 0 1 1 12 6.5a2.5 2.5 0 0 1 0 5z"/></svg>
        <span>2750 Harbor Point Dr Suite 3B<br>Bayview, Florida&nbsp; 34000</span>
      </li>
    </ul>

    <div class="person">
      <p class="person__name">FULL NAME</p>
      <p class="person__role">POSITION</p>
    </div>
  </section>

  <section class="card card--back" aria-label="Business card back">
    <div class="sheen"></div>
    <div class="brand">
      <span class="brand__dot"></span>
      <span class="brand__name">Reef Harbor Aquatics</span>
    </div>
  </section>

</main>
</body>
</html>
```